Corvane Care Group Presentation Folder, for Cancer Awareness, VERY COLORFUL AND MODERN

Presentation Folder I know pretty much what i want so it should be very eazy , I have included files from folders I use now rebrand them to my new company they will be fine, no sense re creating the wheel
Full Bleed Size
20.87" x 16.68"
53 x 42.4 cm
6260 x 5004 pixels
Document Trim Size
20.75" x 16.56"
52.7 x 42.1 cm
6225 x 4969 pixels
Updates

Low design quality

Industry/Entity Type

Medical

Font styles to use
Serif

Colors

Designer to choose colors to be used in the design.

Requirements
Must have
• really I am not looking for some one to redesign, we like our folder front page and would like to see new word information added., there are two folder front pages to choose from
• So Keep the original front page and redesign the back page and the pockets
• Can Make your Design off of one of the ones I already uploaded
Nice to have
• Keep the same color schemes, Keep the original front page and redesign the back page and the pockets
Should not have
• DO not recreate the front covers, use what I gave you and just rebrand

```html
<!DOCTYPE html>
<html lang="en">
<head>
<meta charset="UTF-8">
<title>Corvane Care Group — Hereditary Cancer Screening Folder</title>
<link href="https://fonts.googleapis.com/css2?family=Raleway:wght@300;400;500;600&display=swap" rel="stylesheet">
<style>
  :root {
    --stage: #c9d1d3;
    --pink: #f28cc8;
    --pink-deep: #e97bbd;
    --cyan: #5ec8df;
    --cyan-pale: #d6f1f6;
    --blue: #2d3fd6;
    --grey-band: #a7aaad;
    --grey-text: #8a8e92;
    --ink: #2b2f33;
    --navy: #1e2d7a;
    --white: #ffffff;
  }
  * { box-sizing: border-box; margin: 0; padding: 0; }
  html, body { width: 1200px; height: 1200px; overflow: hidden; }
  body {
    background: var(--stage);
    font-family: "Raleway", sans-serif;
    position: relative;
  }
  .folder-spread {
    position: absolute;
    left: 40px; top: 152px;
    width: 1120px; height: 896px;
    display: flex;
    box-shadow: 0 10px 30px rgba(0,0,0,.15);
  }
  .panel { position: relative; width: 560px; height: 896px; overflow: hidden; }

  /* Back panel */
  .back-panel {
    background: linear-gradient(160deg, var(--white) 0%, var(--cyan-pale) 30%, #9fdfec 65%, var(--cyan) 100%);
  }
  .back-panel .accent-band {
    position: absolute; left: 0; top: 110px; width: 100%; height: 42px;
    background: linear-gradient(90deg, var(--pink) 0%, var(--pink-deep) 100%);
  }
  .back-panel .intro-copy {
    position: absolute; left: 50px; top: 196px; width: 470px;
    font-size: 13.5px; line-height: 1.45; color: var(--ink);
  }
  .back-panel .intro-copy .lead { color: var(--blue); }
  .back-panel .headline {
    position: absolute; left: 90px; top: 340px;
    font-size: 25px; font-weight: 400; color: var(--blue);
  }
  .back-panel .affirmations {
    position: absolute; left: 92px; top: 378px;
    font-size: 17px; line-height: 1.35; color: var(--grey-text); font-weight: 400;
  }
  .back-panel .family-photo {
    position: absolute; left: 0; bottom: 0; width: 100%; height: 370px;
    background: linear-gradient(180deg, rgba(140,215,232,0) 0%, #a9e0ea 35%, #e3ecea 62%, #efe4cf 100%);
  }

  /* Front panel */
  .front-panel { background: var(--white); }
  .front-panel .title-band {
    position: absolute; left: 0; top: 62px; width: 560px; height: 44px;
    background: var(--pink);
    color: var(--white);
    font-size: 21px; font-weight: 400; letter-spacing: 3px;
    display: flex; align-items: center; justify-content: center;
  }
  .front-panel .subtitle-band {
    position: absolute; left: 70px; top: 106px; width: 420px; height: 28px;
    background: var(--grey-band);
    color: var(--white);
    font-size: 11px; letter-spacing: 2px;
    display: flex; align-items: center; justify-content: center;
  }
  .front-panel .tagline {
    position: absolute; left: 60px; top: 154px; width: 440px;
    text-align: center; font-size: 13px; line-height: 1.3; color: var(--blue);
  }
  .front-panel .family-photo {
    position: absolute; left: 40px; top: 212px; width: 480px; height: 370px;
    background: linear-gradient(150deg, #f2f2f2 0%, #bdbdbd 45%, #7c7c7c 75%, #d9d9d9 100%);
  }
  .front-panel .footer-band {
    position: absolute; left: 0; top: 600px; width: 560px; height: 46px;
    background: var(--grey-band);
    color: var(--white);
    font-size: 13px; letter-spacing: 2px;
    display: flex; align-items: center; justify-content: flex-end;
    padding-right: 70px;
  }
  .front-panel .brand {
    position: absolute; left: 70px; top: 618px;
    display: flex; align-items: center; gap: 12px;
  }
  .front-panel .brand-dot {
    width: 62px; height: 62px; border-radius: 50%;
    background: var(--white); border: 4px solid var(--navy);
  }
  .front-panel .brand-name {
    margin-top: 40px;
    font-size: 14px; font-weight: 600; color: var(--navy);
  }
</style>
</head>
<body>
  <main class="folder-spread">
    <section class="panel back-panel">
      <div class="accent-band"></div>
      <p class="intro-copy">
        <span class="lead">Hereditary cancer screening</span> provides vital information to help people with a strong personal or family history of cancer understand their own risk of developing the disease. With this information, they can take steps to Potentially Prevent Cancer, Delay the Onset of Cancer or Catch it at an Earlier stage when outcomes and survival rates are Better.
      </p>
      <h2 class="headline">Don’t be Afraid of the Answer:</h2>
      <p class="affirmations">
        Knowledge is Power and Power Eradicates Fear.<br>
        When You are Fearless,<br>
        You Will Make all the Right Choices!
      </p>
      <div class="family-photo" role="img" aria-label="Photo of a three-generation family walking hand in hand on a sunny beach"></div>
    </section>

    <section class="panel front-panel">
      <h1 class="title-band">HEREDITARY CANCER SCREENING</h1>
      <div class="subtitle-band">DOCTORS ARE THE GATEKEEPERS TO GENETIC TESTING</div>
      <p class="tagline">We have an obligation to help patients understand genetic risk<br>and how testing can guide health care decisions.</p>
      <div class="family-photo" role="img" aria-label="Black and white photo of a family sharing a meal at an outdoor table"></div>
      <div class="footer-band">THE TEST YOU ORDER FOR YOUR PATIENTS</div>
      <div class="brand">
        <span class="brand-dot"></span>
        <span class="brand-name">Corvane Care Group</span>
      </div>
    </section>
  </main>
</body>
</html>
```